Business Card for: Keelwright Financial Advisory Services Inc.

provide strategic financial advisory services to companies in the areas of corporate finance, mergers and acquisitions, executive coaching and strategic planning

Target Market(s)

Companies, banks, accountants, lawyers

Industry/Entity Type

High end business consulting in corporate finance, mergers and acquisitions, consulting

Contact Information for Business Card

Name of company, Name: xxxxxx xxxxxx , CEO, - phone number: 1-xxx-xxx-xxxx, - email address,

Requirements
Must have
• Must be professional and simple.
Nice to have
• simple, straight graphics, must give the impression that we are trustworthy, professional, competent
Should not have
• loud colors, loud design features

```html
<!DOCTYPE html>
<html lang="en">
<head>
<meta charset="utf-8">
<title>Keelwright Financial Advisory Services Inc. — Business Card</title>
<link rel="stylesheet" href="https://fonts.googleapis.com/css2?family=Montserrat:wght@600;700&family=Open+Sans:wght@300;400&display=swap">
<style>
  :root {
    --board: #a9b1cc;
    --label: #4a6290;
    --card: #0b1424;
    --card-edge: #0e192c;
    --pattern: #12233a;
    --gold: #f5a01e;
    --gold-soft: #f2a331;
    --ink: #0b1424;
  }
  * { box-sizing: border-box; margin: 0; padding: 0; }
  html, body { width: 1084px; height: 1200px; overflow: hidden; }
  body { background: var(--board); position: relative; font-family: "Open Sans", sans-serif; }

  .side-label {
    position: absolute; left: 122px;
    font-family: "Open Sans", sans-serif; font-weight: 400;
    font-size: 40px; color: var(--label); letter-spacing: 0.5px;
  }
  .side-label--front { top: 36px; }
  .side-label--back { top: 616px; }

  .card {
    position: absolute; left: 122px; width: 840px; height: 480px;
    background: var(--card); overflow: hidden;
  }
  .card--front { top: 100px; }
  .card--back { top: 680px; }

  .brand { position: absolute; display: flex; align-items: center; gap: 14px; }
  .brand__dot {
    width: 40px; height: 40px; border-radius: 50%;
    border: 4px solid var(--gold); flex: none;
  }
  .brand__text { display: flex; flex-direction: column; }
  .brand__name {
    font-family: "Montserrat", sans-serif; font-weight: 700;
    font-size: 34px; line-height: 1; color: var(--gold);
  }
  .brand__tagline {
    font-family: "Open Sans", sans-serif; font-weight: 400;
    font-size: 17px; line-height: 1.2; color: var(--gold); margin-top: 4px;
  }
  .card--front .brand { left: 72px; top: 204px; }
  .card--back .brand { left: 50%; top: 50%; transform: translate(-50%, -50%); }

  .divider {
    position: absolute; left: 418px; top: 50px;
    width: 5px; height: 382px; background: var(--gold);
  }

  .name-tab {
    position: absolute; left: 466px; top: 129px; width: 374px; height: 91px;
    background: var(--gold); border-radius: 46px 0 0 46px;
    display: flex; flex-direction: column; justify-content: center; align-items: flex-end;
    padding-right: 28px;
  }
  .name-tab__name {
    font-family: "Montserrat", sans-serif; font-weight: 700;
    font-size: 29px; line-height: 1.1; color: var(--ink);
  }
  .name-tab__role {
    font-family: "Open Sans", sans-serif; font-weight: 400;
    font-size: 21px; line-height: 1.1; color: var(--ink);
  }

  .contact { position: absolute; right: 30px; display: flex; align-items: center; gap: 18px; }
  .contact--phone { top: 248px; }
  .contact--email { top: 292px; }
  .contact__text {
    font-family: "Open Sans", sans-serif; font-weight: 300;
    font-size: 22px; color: var(--gold-soft);
  }
  .contact__icon { width: 24px; height: 24px; fill: var(--gold); }

  .back-pattern { position: absolute; inset: 0; background: linear-gradient(135deg, var(--card-edge), var(--pattern) 50%, var(--card-edge)); }
</style>
</head>
<body>
  <div class="side-label side-label--front">front</div>
  <section class="card card--front">
    <div class="brand">
      <span class="brand__dot"></span>
      <div class="brand__text">
        <span class="brand__name">Keelwright</span>
        <span class="brand__tagline">Financial Advisory Services Inc.</span>
      </div>
    </div>
    <div class="divider"></div>
    <div class="name-tab">
      <span class="name-tab__name">Your Name Here</span>
      <span class="name-tab__role">CEO</span>
    </div>
    <div class="contact contact--phone">
      <span class="contact__text">1-XXX-XXX-XXXX</span>
      <svg class="contact__icon" viewBox="0 0 24 24" aria-hidden="true"><path d="M6.6 10.8a15.1 15.1 0 0 0 6.6 6.6l2.2-2.2a1 1 0 0 1 1-.25 11.4 11.4 0 0 0 3.6.57 1 1 0 0 1 1 1V20a1 1 0 0 1-1 1A17 17 0 0 1 3 4a1 1 0 0 1 1-1h3.5a1 1 0 0 1 1 1c0 1.25.2 2.45.57 3.6a1 1 0 0 1-.25 1z"/></svg>
    </div>
    <div class="contact contact--email">
      <span class="contact__text">email@company.com</span>
      <svg class="contact__icon" viewBox="0 0 24 24" aria-hidden="true"><path d="M2 5h20v2.2l-10 6-10-6z"/><path d="M2 9.6l10 6 10-6V19H2z"/></svg>
    </div>
  </section>

  <div class="side-label side-label--back">Back</div>
  <section class="card card--back">
    <div class="back-pattern" role="img" aria-label="Faint navy wave pattern covering the back of the card"></div>
    <div class="brand">
      <span class="brand__dot"></span>
      <div class="brand__text">
        <span class="brand__name">Keelwright</span>
        <span class="brand__tagline">Financial Advisory Services Inc.</span>
      </div>
    </div>
  </section>
</body>
</html>
```